Women's Health - Hormone Imbalance, Menopause, Perimenopause.

We need a poster to match a letter that will be sent out. So people see the poster in store they are reminded about the letter and the newspaper ad.
The Poster is advertising a holistic approach to treating menopause, perimenopause and women's health in general specifically hormonal imbalance.
This it the writing required on the poster
"Are you feeling out of sorts? Is your body changing? Could it be your hormones?
If you’re experiencing changes due to hormonal imbalances, it’s important to consult with a qualified medical professional who understands your needs.
Karim Nasser, the uBlendwell Apothecary, can help. He has practiced pharmacy and nutritional medicine, helping people with hormone imbalances using a holistic approach for over 18 years.
Together, we look at issues around Hormonal Imbalance, Perimenopause and Menopause. To start, we take a profile of your sex hormones, Adrenals, Thyroids and Metabolic Pathways to see how we can best remedy the situation. Karim uses a holistic approach that treats you as a whole – not just the symptoms – for overall better wellness.
Want to know more? Karim is available for consultation on Wednesday Mornings at Red Gully Pharmacy and Thursday Mornings at Fernbrook Pharmacy.
SPECIAL OFFER! Make a booking for one session ($60) and get another session free! This limited-time package includes an initial consultation, historical hormone profile, follow-up consultation and wellness action plan.
To book an appointment with Karim, call 1300 462 851 today."
Pictures required to correspond with the writing. I've also uploaded my logo
Industry/Entity Type
Pharmacy
Font styles to use
Requirements
Must have
- Photos/Images to match the writing. Need women who are suffering from menopause with symptoms such as hot flashes, night sweats, anxiety, depression, fatigue, loss of libido, insomnia.
Nice to have
- Integrative Medicine, tailored medicine approach, Natural, approach, unique, tailor made solution

```html
<!DOCTYPE html>
<html lang="en">
<head>
<meta charset="utf-8">
<title>Hormone Health Poster</title>
<link href="https://fonts.googleapis.com/css2?family=Open+Sans:wght@300;400&family=PT+Sans:ital,wght@0,400;0,700;1,400&family=Oswald:wght@300;600&display=swap" rel="stylesheet">
<style>
  :root {
    --page-bg: #e6e6e8;
    --pink-light: #f9b3cf;
    --pink-mid: #f483b0;
    --pink-deep: #f0437f;
    --white: #ffffff;
    --cyan: #3fe6f4;
    --cyan-soft: #8ff0fa;
    --ink: #111111;
    --brand-blue: #1f3f8f;
  }
  * { margin: 0; padding: 0; box-sizing: border-box; }
  html, body { width: 1200px; height: 1200px; overflow: hidden; }
  body {
    background: var(--page-bg);
    font-family: "PT Sans", Arial, sans-serif;
    position: relative;
  }
  .poster {
    position: absolute;
    left: 221px; top: 48px;
    width: 716px; height: 1105px;
    overflow: hidden;
    background: var(--pink-mid);
  }
  .poster__backdrop { position: absolute; left: 0; top: 0; width: 716px; height: 1051px; }

  .headline {
    position: absolute; left: 0; top: 26px; width: 716px;
    text-align: center; color: var(--white);
    font-family: "Open Sans", Arial, sans-serif;
    font-weight: 300; font-size: 42px; line-height: 50px;
    letter-spacing: -0.8px; white-space: nowrap;
  }

  .intro {
    position: absolute; left: 40px; width: 340px;
    text-align: center; color: var(--white);
    font-size: 15.5px; line-height: 24.6px; white-space: nowrap;
  }
  .intro em { font-style: italic; font-size: 16.5px; }
  .intro--lead { top: 277px; }
  .intro--name { top: 414px; font-size: 24px; line-height: 34px; }
  .intro--bio { top: 448px; }
  .intro--process { top: 595px; }
  .intro--approach { top: 766px; }

  .portrait {
    position: absolute; left: 403px; top: 282px; width: 258px; height: 334px;
  }

  .enquiry {
    position: absolute; left: 382px; width: 300px;
    text-align: center; color: var(--white); white-space: nowrap;
  }
  .enquiry__title {
    top: 652px; color: var(--cyan-soft);
    font-family: "Open Sans", Arial, sans-serif;
    font-size: 28px; font-weight: 400; line-height: 38px; letter-spacing: -0.5px;
  }
  .enquiry__name { top: 688px; font-size: 19px; line-height: 30px; }
  .enquiry__times { top: 718px; font-size: 15.5px; line-height: 24.6px; }

  .offer-rule {
    position: absolute; left: 59px; width: 609px; height: 0;
    border-top: 1px dashed rgba(255,255,255,0.75);
  }
  .offer-rule--top { top: 884px; }
  .offer-rule--bottom { top: 990px; }
  .offer__box {
    position: absolute; left: 59px; top: 899px; width: 609px; height: 89px;
    background: var(--white);
  }
  .offer__tag { position: absolute; left: 46px; top: 901px; width: 140px; height: 75px; }
  .offer__label {
    position: absolute; left: 58px; top: 903px; width: 112px;
    font-family: "Oswald", "Arial Narrow", sans-serif; color: var(--cyan);
    text-transform: uppercase; white-space: nowrap;
  }
  .offer__label-top { display: block; font-weight: 300; font-size: 29px; line-height: 32px; }
  .offer__label-bottom { display: block; font-weight: 600; font-size: 33px; line-height: 36px; }
  .offer__copy {
    position: absolute; left: 182px; top: 903px; width: 480px;
    text-align: center; color: var(--ink); white-space: nowrap;
  }
  .offer__deal { font-size: 15px; font-weight: 700; line-height: 22px; letter-spacing: -0.2px; }
  .offer__detail { font-size: 13px; line-height: 18px; margin-top: 6px; }

  .cta {
    position: absolute; left: 0; top: 1004px; width: 716px;
    text-align: center; color: var(--white);
    font-family: "Open Sans", Arial, sans-serif;
    font-weight: 300; font-size: 22px; line-height: 34px;
    letter-spacing: -0.4px; white-space: nowrap;
  }
  .cta strong { font-weight: 400; font-family: "PT Sans", Arial, sans-serif; font-size: 24px; font-weight: 700; letter-spacing: 0; }

  .footer {
    position: absolute; left: 0; top: 1051px; width: 716px; height: 54px;
    background: var(--white);
  }
  .brand {
    position: absolute; right: 46px; top: 14px;
    display: flex; align-items: center; gap: 8px;
    color: var(--brand-blue); font-weight: 700; font-size: 20px; white-space: nowrap;
  }
  .brand__dot { width: 16px; height: 16px; border-radius: 50%; background: var(--brand-blue); }
</style>
</head>
<body>
  <main class="poster">
    <svg class="poster__backdrop" role="img" aria-label="Soft pink photo of a woman holding her lower back, and a flowing wave shape behind the text" viewBox="0 0 716 1051">
      <defs>
        <radialGradient id="bodyGlow" cx="0.5" cy="0.2" r="0.6">
          <stop offset="0" stop-color="#fbc6da"/>
          <stop offset="0.55" stop-color="#f692ba"/>
          <stop offset="1" stop-color="#f483b0" stop-opacity="0"/>
        </radialGradient>
        <linearGradient id="waveFill" x1="0" y1="0" x2="0" y2="1">
          <stop offset="0" stop-color="#f25590"/>
          <stop offset="1" stop-color="#ef3e7e"/>
        </linearGradient>
      </defs>
      <rect x="0" y="0" width="716" height="760" fill="url(#bodyGlow)"/>
      <path d="M0 500 C180 450 420 500 716 455" fill="none" stroke="#ffffff" stroke-opacity="0.35" stroke-width="2"/>
      <path d="M0 540 C220 480 460 540 716 485" fill="none" stroke="#ffffff" stroke-opacity="0.25" stroke-width="1.5"/>
      <path d="M0 800 C170 700 400 640 716 610 L716 1051 L0 1051 Z" fill="url(#waveFill)"/>
      <path d="M0 700 C200 630 420 720 716 660" fill="none" stroke="#ffffff" stroke-opacity="0.3" stroke-width="1.5"/>
    </svg>

    <h1 class="headline">Are you feeling out of sorts?<br>Is your body changing?<br>Could it be your hormones?</h1>

    <p class="intro intro--lead">If you’re experiencing changes due to<br><em>hormonal imbalances,</em><br>it’s important to consult with a qualified<br>medical professional who understands<br>your needs.</p>
    <p class="intro intro--name">Karim Nasser,</p>
    <p class="intro intro--bio">the uBlendwell Apothecary, can help.<br>He has practiced pharmacy and<br>nutritional medicine, helping people with<br>hormone imbalances using a<br>holistic approach for over 18 years.</p>
    <p class="intro intro--process">Together, we look at issues around<br>Hormonal Imbalance, Perimenopause and<br>Menopause. To start, we take a profile of<br>your sex hormones, Adrenals, Thyroids<br>and Metabolic Pathways to see how we<br>can best remedy the situation.</p>
    <p class="intro intro--approach">Karim uses a holistic approach that treats<br>you as a whole – not just the symptoms –<br>for overall better wellness.</p>

    <svg class="portrait" role="img" aria-label="Photo of a woman with a headache, hands pressed to her temples" viewBox="0 0 258 334">
      <defs>
        <linearGradient id="portraitFill" x1="0" y1="0" x2="0" y2="1">
          <stop offset="0" stop-color="#e4e8ee"/>
          <stop offset="0.55" stop-color="#cfc3b8"/>
          <stop offset="1" stop-color="#b9aa9c"/>
        </linearGradient>
      </defs>
      <rect width="258" height="334" fill="url(#portraitFill)"/>
    </svg>

    <h2 class="enquiry enquiry__title">want to know more?</h2>
    <p class="enquiry enquiry__name">Karim Nasser</p>
    <p class="enquiry enquiry__times">is available for consultation on<br>Wednesday Mornings<br>at Red Gully Pharmacy<br>and<br>Thursday Mornings<br>at Fernbrook Pharmacy</p>

    <div class="offer-rule offer-rule--top"></div>
    <div class="offer__box"></div>
    <svg class="offer__tag" viewBox="0 0 140 75" aria-hidden="true">
      <polygon points="0,0 124,0 140,37.5 124,75 0,75" fill="#111111"/>
    </svg>
    <p class="offer__label"><span class="offer__label-top">Special</span><span class="offer__label-bottom">Offer</span></p>
    <div class="offer__copy">
      <p class="offer__deal">Make a booking for one session ($60) and get another session free!</p>
      <p class="offer__detail">This limited-time package includes an initial consultation,<br>historical hormone profile, follow-up consultation and wellness action plan.</p>
    </div>
    <div class="offer-rule offer-rule--bottom"></div>

    <p class="cta">To book an appointment with Karim, <strong>Call 1300 462 851</strong> today!</p>

    <footer class="footer">
      <div class="brand"><span class="brand__dot"></span>uBlendwell Apothecary</div>
    </footer>
  </main>
</body>
</html>
```